Infographic for venture capital "investment adviser" model

We need an infographic for users to easily visualize and grasp what is meant by a "investment adviser" model. The attached .pdf has the copy and my (very bad) rough design of the graphic. Needs to be professionally done now.

Description of Venture Capital: a venture capitalist creates a "fund", they then go raise money from investors for that fund. Once they have money, they then invest it in various companies or assets. As money com comes back to the fund from the investments, the venture capitalist pays the funds investors (and themselves).

A venture capitalist will usually manage multiple "funds". That's why there is a management company (the VC) that is hired by each fund they create. The VC management company is paid an annual fee of 2%, and then they also get 20% of the profits - that's what the "2%/20%" represents in the graphic.

Target Market(s)

Venture capitalists, investment advisers, wall street brokers

Industry/Entity Type

Venture Capital

Font styles to use
Serif

Colors
f37122
f68d4c
3276b5

Requirements
Must have
• Our logo (attached)
• Display 3 different funds, all being managed by a single entity
• Fyi - I just uploaded a new graphic of what the "website" should look like (can be similar, doesn't have to be this image...just something to show a crowdfunding website)
Nice to have
• Neat representations of investors and of a funds portfolio companies

```html
<!DOCTYPE html>
<html lang="en">
<head>
<meta charset="utf-8">
<title>Funding Platform – VC Investment Adviser Model</title>
<link rel="stylesheet" href="https://fonts.googleapis.com/css2?family=Arimo:wght@700&family=PT+Serif:ital,wght@0,400;0,700;1,400&family=Open+Sans:wght@400;700&display=swap">
<style>
  :root {
    --band-blue: #3a73a8;
    --fund-blue: #3276b5;
    --orange-deep: #f37122;
    --orange-soft: #f68d4c;
    --orange-box: #ef7d33;
    --white: #ffffff;
    --ink: #1d1d1d;
    --note-blue: #2f6db0;
  }
  html, body {
    margin: 0;
    padding: 0;
    overflow: hidden;
    background: var(--white);
  }
  .canvas {
    width: 1200px;
    height: 854px;
    display: block;
  }
  .title-main { font-family: "Arimo", Arial, sans-serif; font-weight: 700; font-size: 50px; fill: var(--white); }
  .title-sub { font-family: "PT Serif", Georgia, serif; font-weight: 700; font-size: 31px; fill: var(--white); }
  .serif { font-family: "PT Serif", Georgia, serif; }
  .sans { font-family: "Open Sans", Arial, sans-serif; }
  .box-heading { font-family: "PT Serif", Georgia, serif; font-weight: 700; font-size: 18px; fill: var(--ink); }
  .box-body { font-family: "Open Sans", Arial, sans-serif; font-weight: 700; font-size: 15px; fill: var(--ink); }
  .box-caption { font-family: "Open Sans", Arial, sans-serif; font-style: italic; font-size: 14px; fill: var(--ink); }
  .fee-label { font-family: "Open Sans", Arial, sans-serif; font-weight: 700; font-size: 21px; fill: var(--ink); }
  .link-label { font-family: "Open Sans", Arial, sans-serif; font-weight: 700; font-size: 13px; fill: var(--ink); }
  .fund-title { font-family: "PT Serif", Georgia, serif; font-weight: 700; font-size: 30px; fill: var(--white); }
  .fund-sub { font-family: "PT Serif", Georgia, serif; font-size: 19px; fill: var(--white); }
  .portfolio-head { font-family: "PT Serif", Georgia, serif; font-weight: 700; font-size: 14px; fill: var(--ink); }
  .portfolio-body { font-family: "Open Sans", Arial, sans-serif; font-size: 12px; fill: var(--ink); }
  .investor-label { font-family: "PT Serif", Georgia, serif; font-size: 15px; fill: var(--fund-blue); }
  .footnote { font-family: "Open Sans", Arial, sans-serif; font-weight: 700; font-size: 12px; fill: var(--note-blue); }
  .copyright { font-family: "Open Sans", Arial, sans-serif; font-size: 12px; fill: var(--ink); }
  .brand-name { font-family: "Open Sans", Arial, sans-serif; font-weight: 700; font-size: 21px; fill: var(--fund-blue); }
  .bullet { fill: var(--orange-soft); }
  .flow-fee { stroke: var(--white); stroke-width: 2; fill: none; }
  .flow-dark { stroke: var(--ink); stroke-width: 2; fill: none; }
</style>
</head>
<body>
<svg class="canvas" viewBox="0 0 1200 854" xmlns="http://www.w3.org/2000/svg">
  <defs>
    <linearGradient id="bg-gradient" x1="0" y1="0" x2="0" y2="1">
      <stop offset="0" stop-color="#f4a066"/>
      <stop offset="1" stop-color="#ee8536"/>
    </linearGradient>
    <marker id="head-white" viewBox="0 0 10 10" refX="8" refY="5" markerWidth="7" markerHeight="7" orient="auto-start-reverse">
      <path d="M0 0 L10 5 L0 10 z" fill="#ffffff"/>
    </marker>
    <marker id="head-dark" viewBox="0 0 10 10" refX="8" refY="5" markerWidth="6" markerHeight="6" orient="auto-start-reverse">
      <path d="M0 0 L10 5 L0 10 z" fill="#1d1d1d"/>
    </marker>
  </defs>

  <!-- background -->
  <rect class="backdrop" width="1200" height="854" fill="url(#bg-gradient)"/>

  <!-- header band -->
  <g class="header">
    <rect width="1200" height="94" fill="var(--band-blue)"/>
    <text class="title-main" x="36" y="66">FUNDING PLATFORM</text>
    <text class="title-sub" x="612" y="60">VC “Investment !dviser” Model *</text>
  </g>

  <!-- management fee flows -->
  <g class="fee-flows">
    <line class="flow-fee" x1="382" y1="616" x2="554" y2="218" marker-end="url(#head-white)"/>
    <line class="flow-fee" x1="619" y1="614" x2="619" y2="218" marker-end="url(#head-white)"/>
    <line class="flow-fee" x1="795" y1="624" x2="692" y2="218" marker-end="url(#head-white)"/>
    <text class="fee-label" transform="translate(494 348) rotate(-74)">2%/20%</text>
    <text class="fee-label" transform="translate(610 362) rotate(-90)">2%/20%</text>
    <text class="fee-label" transform="translate(720 366) rotate(-104)" text-anchor="end"><tspan>2%/20%</tspan></text>
  </g>

  <!-- technology & marketing flows -->
  <g class="tech-flows">
    <line class="flow-dark" x1="342" y1="620" x2="271" y2="494" marker-end="url(#head-dark)"/>
    <line class="flow-dark" x1="544" y1="638" x2="268" y2="462" marker-end="url(#head-dark)"/>
    <line class="flow-dark" x1="766" y1="632" x2="282" y2="437" marker-end="url(#head-dark)"/>
    <text class="link-label" transform="translate(283 502) rotate(61)">Technology &amp; Mktg</text>
    <text class="link-label" transform="translate(292 472) rotate(33)">Technology &amp; Mktg</text>
    <text class="link-label" transform="translate(450 492) rotate(22)">Technology &amp; Mktg</text>
  </g>

  <!-- management company -->
  <g class="management-box">
    <rect x="520" y="118" width="208" height="90" rx="10" fill="var(--orange-box)" stroke="var(--white)" stroke-width="2"/>
    <text class="box-heading" x="624" y="143" text-anchor="middle">VENTURES</text>
    <text class="box-heading" x="624" y="163" text-anchor="middle" font-size="15">IA Management Group</text>
    <text class="box-caption" x="546" y="181" font-size="12">fee on assets of the funds,</text>
    <text class="box-caption" x="585" y="197" font-size="12">Plus carried interest</text>
  </g>

  <!-- website box -->
  <g class="website-box">
    <rect x="88" y="353" width="184" height="129" rx="14" fill="var(--white)"/>
    <text class="box-heading" x="102" y="381" font-size="16">Website <tspan font-style="italic" font-weight="700">(aka</tspan></text>
    <text class="box-heading" x="102" y="401" font-size="16" font-style="italic">“Funding Platform”)</text>
    <text class="box-caption" x="102" y="420">Functions:</text>
    <circle class="bullet" cx="105" cy="436" r="4.5"/>
    <text class="box-body" x="116" y="441">Advertising/Mktg</text>
    <circle class="bullet" cx="105" cy="458" r="4.5"/>
    <text class="box-body" x="116" y="463">SaaS</text>
  </g>

  <!-- broker-dealer box -->
  <g class="broker-box">
    <rect x="955" y="592" width="235" height="236" rx="22" fill="var(--white)"/>
    <text class="box-heading" x="1072" y="631" text-anchor="middle">Broker-Dealer -</text>
    <rect x="975" y="648" width="13" height="13" fill="var(--fund-blue)"/>
    <text class="brand-name" x="996" y="662">CapitalBridge</text>
    <text class="box-caption" x="976" y="690">Functions:</text>
    <circle class="bullet" cx="980" cy="707" r="4.5"/>
    <text class="box-body" x="991" y="712">Escrow</text>
    <circle class="bullet" cx="980" cy="730" r="4.5"/>
    <text class="box-body" x="991" y="735">State blue sky</text>
    <circle class="bullet" cx="980" cy="753" r="4.5"/>
    <text class="box-body" x="991" y="758">AML</text>
    <circle class="bullet" cx="980" cy="776" r="4.5"/>
    <text class="box-body" x="991" y="781">Payment processing</text>
    <circle class="bullet" cx="980" cy="799" r="4.5"/>
    <text class="box-body" x="991" y="804">Etc</text>
  </g>

  <!-- broker-dealer links -->
  <g class="broker-flows">
    <line class="flow-dark" x1="948" y1="654" x2="903" y2="654" marker-end="url(#head-dark)"/>
    <line class="flow-dark" x1="556" y1="730" x2="944" y2="703" marker-end="url(#head-dark)"/>
    <line class="flow-dark" x1="683" y1="742" x2="944" y2="714" marker-end="url(#head-dark)"/>
    <line class="flow-dark" x1="915" y1="764" x2="946" y2="738" marker-end="url(#head-dark)"/>
  </g>

  <!-- funds label -->
  <text class="box-heading sans" x="176" y="669" font-family="Open Sans, Arial, sans-serif" font-size="17">The Funds:</text>

  <!-- funds -->
  <g class="fund fund-1">
    <ellipse cx="370" cy="652" rx="82" ry="37" fill="var(--fund-blue)"/>
    <text class="fund-title" x="370" y="664" text-anchor="middle">FUND</text>
    <text class="fund-sub" x="370" y="684" text-anchor="middle">SPV 1</text>
  </g>
  <g class="fund fund-2">
    <ellipse cx="620" cy="652" rx="82" ry="37" fill="var(--fund-blue)"/>
    <text class="fund-title" x="620" y="664" text-anchor="middle">FUND</text>
    <text class="fund-sub" x="620" y="684" text-anchor="middle">SPV 2</text>
  </g>
  <g class="fund fund-3">
    <ellipse cx="818" cy="652" rx="78" ry="37" fill="var(--fund-blue)"/>
    <text class="fund-title" x="818" y="664" text-anchor="middle">FUND</text>
    <text class="fund-sub" x="818" y="684" text-anchor="middle">SPV 3</text>
  </g>

  <!-- fund to portfolio / investor links -->
  <g class="fund-flows">
    <line class="flow-dark" x1="318" y1="690" x2="303" y2="712" marker-end="url(#head-dark)"/>
    <line class="flow-dark" x1="403" y1="707" x2="418" y2="736" marker-start="url(#head-dark)" marker-end="url(#head-dark)"/>
    <line class="flow-dark" x1="562" y1="690" x2="548" y2="712" marker-end="url(#head-dark)"/>
    <line class="flow-dark" x1="630" y1="707" x2="648" y2="736" marker-start="url(#head-dark)" marker-end="url(#head-dark)"/>
    <line class="flow-dark" x1="806" y1="712" x2="788" y2="745" marker-end="url(#head-dark)"/>
    <line class="flow-dark" x1="866" y1="697" x2="886" y2="745" marker-start="url(#head-dark)" marker-end="url(#head-dark)"/>
  </g>

  <!-- portfolios -->
  <g class="portfolio portfolio-1">
    <circle cx="262" cy="749" r="40" fill="var(--white)" stroke="var(--white)" stroke-width="9" stroke-dasharray="4 4"/>
    <text class="portfolio-head" x="262" y="743" text-anchor="middle">Portfolio:</text>
    <text class="portfolio-body" x="262" y="760" text-anchor="middle">Company</text>
    <text class="portfolio-body" x="262" y="776" text-anchor="middle">or Asset</text>
  </g>
  <g class="portfolio portfolio-2">
    <circle cx="515" cy="749" r="40" fill="var(--white)" stroke="var(--white)" stroke-width="9" stroke-dasharray="4 4"/>
    <text class="portfolio-head" x="515" y="743" text-anchor="middle">Portfolio:</text>
    <text class="portfolio-body" x="515" y="760" text-anchor="middle">Company</text>
    <text class="portfolio-body" x="515" y="776" text-anchor="middle">or Asset</text>
  </g>
  <g class="portfolio portfolio-3">
    <circle cx="762" cy="782" r="40" fill="var(--white)" stroke="var(--white)" stroke-width="9" stroke-dasharray="4 4"/>
    <text class="portfolio-head" x="762" y="776" text-anchor="middle">Portfolio:</text>
    <text class="portfolio-body" x="762" y="793" text-anchor="middle">Company</text>
    <text class="portfolio-body" x="762" y="809" text-anchor="middle">or Asset</text>
  </g>

  <!-- investors -->
  <g class="investors investors-1">
    <rect x="371" y="741" width="87" height="30" rx="4" fill="var(--fund-blue)" role="img" aria-label="Group of five investor figures"/>
    <text class="investor-label" x="414" y="789" text-anchor="middle">Investors</text>
  </g>
  <g class="investors investors-2">
    <rect x="597" y="741" width="87" height="30" rx="4" fill="var(--fund-blue)" role="img" aria-label="Group of five investor figures"/>
    <text class="investor-label" x="640" y="789" text-anchor="middle">Investors</text>
  </g>
  <g class="investors investors-3">
    <rect x="834" y="748" width="86" height="30" rx="4" fill="var(--fund-blue)" role="img" aria-label="Group of five investor figures"/>
    <text class="investor-label" x="877" y="795" text-anchor="middle">Investors</text>
  </g>

  <!-- footer notes -->
  <text class="footnote" x="42" y="818">* Note: NOT intended as legal advice, consult your securities attorney</text>
  <text class="copyright" x="32" y="836">©CapitalBridge Technologies, LLC  2015 All Rights Reserved</text>
</svg>
</body>
</html>
```